Online video and marketing company business cards

Need to get some new business cards designed to fit with our new logo. The cards should be professional, clean and simple.

Cards should have:

Name
Position
2 line address
telephone
mobile
email address
web address

We need to have our logo and if possible say what we do...
ONLINE FILM PRODUCTION & STRATEGY

Industry/Entity Type

Marketing

```html
<!DOCTYPE html>
<html lang="en">
<head>
<meta charset="utf-8">
<title>Lumora Media business cards</title>
<link rel="stylesheet" href="https://fonts.googleapis.com/css2?family=Source+Sans+3:wght@400;600;700&display=swap">
<style>
  :root {
    --page: #e9e4dd;
    --card-white: #ffffff;
    --navy: #0b3f68;
    --navy-deep: #062c4c;
    --navy-light: #14507f;
    --sky: #6ea3c1;
    --ink: #2b2b2b;
    --white: #ffffff;
  }
  * { margin: 0; padding: 0; box-sizing: border-box; }
  html, body { width: 1200px; height: 1024px; overflow: hidden; }
  body {
    background: var(--page);
    font-family: "Source Sans 3", "Myriad Pro", Arial, sans-serif;
    position: relative;
  }
  .card {
    position: absolute;
    border-radius: 36px;
    overflow: hidden;
    box-shadow: 0 10px 22px rgba(0,0,0,0.28);
  }
  .card-front {
    left: 26px; top: 64px; width: 766px; height: 436px;
    background: var(--card-white);
  }
  .front-shapes { position: absolute; inset: 0; }
  .brand {
    position: absolute;
    display: flex; align-items: center;
    font-weight: 600;
    letter-spacing: -0.5px;
    white-space: nowrap;
  }
  .brand-dot { border-radius: 50%; flex: none; }
  .card-front .brand { left: 40px; top: 98px; font-size: 40px; gap: 10px; color: var(--sky); }
  .card-front .brand-dot { width: 36px; height: 36px; background: var(--navy); }
  .contact-list {
    position: absolute; left: 46px; top: 250px;
    list-style: none; color: var(--ink);
    font-size: 20px; line-height: 24.5px;
  }
  .contact-list li { display: flex; align-items: center; gap: 6px; }
  .contact-list svg { width: 15px; height: 15px; fill: var(--navy); flex: none; }
  .person {
    position: absolute; right: 45px; top: 100px; text-align: right; color: var(--white);
  }
  .person-name { font-size: 29px; font-weight: 700; letter-spacing: 0.3px; line-height: 1.1; }
  .person-role { font-size: 19px; font-weight: 400; margin-top: 4px; }
  .address {
    position: absolute; right: 45px; top: 282px; text-align: right;
    color: var(--white); font-size: 21px; line-height: 27px; font-style: normal;
  }
  .card-back {
    left: 362px; top: 534px; width: 778px; height: 444px;
    background: linear-gradient(90deg, var(--navy-deep) 0%, var(--navy-light) 45%, var(--navy-light) 60%, var(--navy-deep) 100%);
  }
  .card-back .brand {
    left: 0; right: 0; top: 196px; justify-content: center;
    font-size: 70px; gap: 14px; color: var(--sky);
  }
  .card-back .brand-dot { width: 56px; height: 56px; background: var(--white); }
  .back-web {
    position: absolute; left: 0; right: 0; top: 378px; text-align: center;
    color: var(--white); font-size: 21px;
  }
</style>
</head>
<body>
  <section class="card card-front" aria-label="Business card front">
    <svg class="front-shapes" viewBox="0 0 766 436" preserveAspectRatio="none">
      <defs>
        <radialGradient id="panelGlow" cx="0.55" cy="0.5" r="0.7">
          <stop offset="0" stop-color="#155585"/>
          <stop offset="1" stop-color="#062c4c"/>
        </radialGradient>
      </defs>
      <path d="M470 0 C 330 90, 330 330, 520 436 L 490 436 C 300 330, 300 90, 440 0 Z" fill="var(--sky)"/>
      <path d="M495 0 C 340 80, 350 330, 560 436 L 535 436 C 330 330, 325 100, 478 0 Z" fill="var(--navy)"/>
      <path d="M505 0 C 355 90, 365 330, 575 436 L 766 436 L 766 0 Z" fill="url(#panelGlow)"/>
    </svg>

    <div class="brand"><span class="brand-dot"></span><span class="brand-name">lumoramedia</span></div>

    <ul class="contact-list">
      <li><svg viewBox="0 0 16 16"><rect x="4" y="1" width="8" height="14" rx="1.5"/></svg>000 000 0000</li>
      <li><svg viewBox="0 0 16 16"><path d="M3 1 L6 1 L7 5 L5 6 C6 9 7 10 10 11 L11 9 L15 10 L15 13 C15 14 14 15 13 15 C6 14 2 10 1 3 C1 2 2 1 3 1 Z"/></svg>+00 0 0000 0000</li>
      <li><svg viewBox="0 0 16 16"><rect x="4" y="1" width="8" height="5"/><rect x="1" y="6" width="14" height="6" rx="1"/><rect x="4" y="10" width="8" height="5"/></svg>+00 0 0000 0000</li>
      <li><svg viewBox="0 0 16 16"><circle cx="8" cy="8" r="7"/></svg>www.lumoramedia.com</li>
      <li><svg viewBox="0 0 16 16"><rect x="1" y="3" width="14" height="10"/><path d="M1 3 L8 9 L15 3" fill="none" stroke="#fff" stroke-width="1.4"/></svg>name@lumoramedia.com</li>
    </ul>

    <div class="person">
      <p class="person-name">MARCUS HALE</p>
      <p class="person-role">Job Title</p>
    </div>

    <address class="address">Your Address Goes Here,<br>City, Zip Code, State,<br>CountryName</address>
  </section>

  <section class="card card-back" aria-label="Business card back">
    <div class="brand"><span class="brand-dot"></span><span class="brand-name">lumoramedia</span></div>
    <p class="back-web">www.lumoramedia.com</p>
  </section>
</body>
</html>
```